We want a business card/punch card for our business. We are including examples of our current business card (we like the front of our business card and not looking to remake it). We need only back side to be designed in form of a punch card (we are including a sample of the punch card we made, but are unsatisfied). For each $180 spend (9 punches) our clients have $20 off.

Colors
886aae

```html
<!DOCTYPE html>
<html lang="en">
<head>
<meta charset="utf-8">
<title>Aurora Practices – Punch Card</title>
<link rel="stylesheet" href="https://fonts.googleapis.com/css2?family=Source+Sans+3:wght@400;600;700&display=swap">
<style>
  :root{
    --bg:#2a2a2c;
    --card:#f7f7f8;
    --violet:#7b3db3;
    --periwinkle:#6874c0;
    --lavender:#886aae;
    --ink:#1e1e22;
    --faint:#e6e6ea;
  }
  *{margin:0;padding:0;box-sizing:border-box}
  html,body{width:1200px;height:900px;overflow:hidden;background:var(--bg);
    font-family:"Source Sans 3",Arial,sans-serif}
  .canvas{position:relative;width:1200px;height:900px}
  .card{position:absolute;width:560px;height:320px;background:var(--card);
    border-radius:18px;overflow:hidden}
  .card--front{left:70px;top:90px}
  .card--back{left:570px;top:490px}

  .wave{position:absolute;inset:0;width:100%;height:100%}

  .punch{position:absolute;width:56px;height:56px;border-radius:50%;
    background:radial-gradient(circle,#ffffff 0 18%,#8c98d4 19% 45%,var(--periwinkle) 46% 100%)}

  .brand{position:absolute;right:40px;top:70px;display:flex;align-items:center;gap:10px}
  .brand__dot{width:30px;height:30px;border-radius:50%;background:var(--violet)}
  .brand__name{font-weight:600;font-size:28px;color:var(--violet);line-height:1}

  .illustration{position:absolute;left:0;top:70px;width:300px;height:250px;
    border-top-right-radius:160px;
    background:linear-gradient(150deg,#c7cbec 0%,#9d86cc 55%,var(--violet) 100%)}

  .watermark{position:absolute;right:-70px;top:140px;transform:rotate(90deg);
    font-size:64px;font-weight:600;color:var(--faint);white-space:nowrap;line-height:1}

  .contact{position:absolute;left:318px;top:50px;color:var(--ink)}
  .contact__names{font-size:22px;font-weight:700;color:var(--violet)}
  .contact__phone{font-size:18px;font-weight:600;color:var(--violet);display:flex;align-items:center;gap:7px;margin-bottom:22px}
  .contact__list{list-style:none;font-size:14px;line-height:1.55}
  .contact__list li{display:flex;align-items:center;gap:7px}
  .icon{width:14px;height:14px;flex:none}
  .icon--square{background:var(--periwinkle);border-radius:2px}
  .icon--circle{background:#d6334a;border-radius:50%}
</style>
</head>
<body>
<div class="canvas">

  <section class="card card--front">
    <svg class="wave" viewBox="0 0 560 320" aria-hidden="true">
      <path d="M0,282 C160,268 300,236 400,168 C445,138 500,122 560,118 L560,320 L0,320 Z" fill="var(--periwinkle)"/>
      <path d="M0,262 C160,252 300,218 392,150 C420,130 448,118 478,108 C448,126 420,142 396,162 C300,232 160,266 0,276 Z" fill="var(--violet)"/>
    </svg>
    <div class="punch" role="img" aria-label="mandala punch spot 1" style="left:40px;top:45px"></div>
    <div class="punch" role="img" aria-label="mandala punch spot 2" style="left:120px;top:30px"></div>
    <div class="punch" role="img" aria-label="mandala punch spot 3" style="left:200px;top:15px"></div>
    <div class="punch" role="img" aria-label="mandala punch spot 4" style="left:70px;top:115px"></div>
    <div class="punch" role="img" aria-label="mandala punch spot 5" style="left:150px;top:100px"></div>
    <div class="punch" role="img" aria-label="mandala punch spot 6" style="left:230px;top:85px"></div>
    <div class="punch" role="img" aria-label="mandala punch spot 7" style="left:100px;top:185px"></div>
    <div class="punch" role="img" aria-label="mandala punch spot 8" style="left:180px;top:170px"></div>
    <div class="punch" role="img" aria-label="mandala punch spot 9" style="left:260px;top:155px"></div>
    <div class="brand">
      <span class="brand__dot"></span>
      <span class="brand__name">Aurora Practices</span>
    </div>
  </section>

  <section class="card card--back">
    <div class="watermark" aria-hidden="true">Aurora Practices</div>
    <div class="illustration" role="img" aria-label="lotus flower with two swans forming a heart around a mandala"></div>
    <div class="contact">
      <p class="contact__names">Dan &amp; Lena</p>
      <p class="contact__phone">
        <svg class="icon" viewBox="0 0 16 16" aria-hidden="true"><path d="M3 2h3l1.5 3.5-2 1.3a8 8 0 0 0 3.7 3.7l1.3-2L14 10v3a1 1 0 0 1-1 1A11 11 0 0 1 2 3a1 1 0 0 1 1-1z" fill="var(--violet)"/></svg>
        555-014-2290
      </p>
      <ul class="contact__list">
        <li><svg class="icon" viewBox="0 0 16 16" aria-hidden="true"><circle cx="8" cy="8" r="6.5" fill="none" stroke="var(--periwinkle)" stroke-width="1.4"/><path d="M1.5 8h13M8 1.5c-3 3.5-3 9.5 0 13M8 1.5c3 3.5 3 9.5 0 13" fill="none" stroke="var(--periwinkle)" stroke-width="1.2"/></svg>www.aurorapractices.com</li>
        <li><svg class="icon" viewBox="0 0 16 16" aria-hidden="true"><rect x="1" y="3" width="14" height="10" rx="1" fill="var(--periwinkle)"/><path d="M1.5 3.5 8 9l6.5-5.5" fill="none" stroke="#fff" stroke-width="1.3"/></svg>info@aurorapractices.com</li>
        <li><span class="icon icon--square"></span>Circlebook.com/AuroraPractices</li>
        <li><span class="icon icon--circle"></span>Gatherup.com/AuroraPractices</li>
      </ul>
    </div>
  </section>

</div>
</body>
</html>
```